Business Postcard Mailer - 2 sided - 6 x 10.5 inches

We will be purchasing multiple designs through this project. We need a postcard mailer for a residential painting business. The final design needs to have the special 15% Off, contact information, company logo, stamp indicia, and list of services. I will provide past examples and any additional logos. Company colors are #34482E and #4A1717. Old samples are provided. Final flat size should be 6 x 10.5 inches. And we will need a return address in the upper left-hand corner of the backside. QMRB Layout Guidelines are attached. 4389 Juniper Ave #7, Waukesha, WI 53947.
Updates

I just guaranteed the project and will be expecting more entries. We will also be purchasing additional designs (4-5) so we want to ensure a good variety.

Target Market(s)

Homeowners

Industry/Entity Type

Painting

Font styles to use
Sans Serif

Requirements
Must have
• Logo and brand colors
Nice to have
• Call to action - Book your free estimate at www.BrightCoatCrew.example or Call now 262-555-0147.

```html
<!DOCTYPE html>
<html lang="en">
<head>
<meta charset="utf-8">
<title>BrightCoat Crew – Spring Special Postcard (Back and Front)</title>
<link href="https://fonts.googleapis.com/css2?family=Josefin+Sans:wght@300;400&family=Hind:wght@400;500&display=swap" rel="stylesheet">
<style>
  :root {
    --brand-green: #34482E;
    --brand-maroon: #4A1717;
    --ink: #3a3a3a;
    --icon: #5a5a5a;
    --paper: #ffffff;
    --backdrop: #ebebeb;
    --rule: #9a9a9a;
    --wood-light: #c3a983;
    --wood-dark: #8a7050;
  }
  * { margin: 0; padding: 0; box-sizing: border-box; }
  html, body { width: 1200px; height: 1200px; overflow: hidden; background: var(--backdrop); }

  .postcard {
    position: absolute; left: 190px;
    width: 1120px; height: 752px;
    transform: scale(0.732); transform-origin: top left;
    background: var(--paper);
    overflow: hidden;
    font-family: "Josefin Sans", sans-serif;
    color: var(--ink);
  }
  .postcard-back { top: 33px; }
  .postcard-front { top: 617px; }

  .photo {
    position: absolute;
    background: linear-gradient(150deg, var(--wood-light) 0%, #b59a74 40%, #d9b450 70%, var(--wood-dark) 100%);
  }

  /* ---------- Back ---------- */
  .contact-panel { position: absolute; left: 0; top: 0; width: 330px; height: 440px; text-align: center; }
  .contact-panel .brand-name {
    position: absolute; left: 0; right: 0; top: 40px;
    font-size: 30px; font-weight: 400; color: var(--brand-maroon); letter-spacing: 1px;
  }
  .contact-panel .top-rule { position: absolute; left: 20px; right: 0; top: 92px; border-top: 2px solid var(--rule); }
  .contact-icon { position: absolute; left: 154px; width: 22px; height: 22px; }
  .contact-line { position: absolute; left: 0; right: 0; color: var(--ink); white-space: nowrap; }
  .contact-line.address { top: 140px; font-size: 20px; line-height: 26px; font-weight: 300; }
  .contact-line.phone { top: 240px; font-size: 36px; font-weight: 300; letter-spacing: 1px; }
  .contact-line.email { top: 326px; font-size: 17px; font-weight: 300; }
  .contact-line.web { top: 394px; font-size: 17px; font-weight: 300; }

  .about-band {
    position: absolute; left: 0; top: 440px; width: 330px; height: 312px;
    background: var(--brand-green); color: var(--paper);
    padding: 34px 28px 0 28px;
  }
  .about-band p { font-size: 19px; line-height: 28px; font-weight: 300; text-align: justify; }

  .postcard-back .photo { left: 330px; top: 0; width: 500px; height: 752px; }

  .cta-panel { position: absolute; left: 830px; top: 0; width: 290px; height: 752px; background: var(--paper); }
  .cta-panel p {
    position: absolute; left: 30px; top: 250px; width: 250px;
    font-size: 36px; line-height: 48px; font-weight: 300; letter-spacing: 2px; color: var(--brand-maroon);
  }

  /* ---------- Front ---------- */
  .services-panel { position: absolute; left: 0; top: 0; width: 403px; height: 100%; }
  .services-panel .top-rule { position: absolute; left: 18px; right: 0; top: 38px; border-top: 2px solid var(--rule); }
  .eyebrow { position: absolute; left: 18px; top: 46px; font-size: 21px; font-weight: 300; color: var(--brand-maroon); letter-spacing: 0.5px; }
  .headline { position: absolute; left: 18px; top: 82px; font-size: 62px; font-weight: 300; color: var(--brand-maroon); letter-spacing: 3px; line-height: 1; }
  .service-list { position: absolute; left: 50px; top: 163px; list-style: none; }
  .service-list li {
    position: relative; font-size: 25px; font-weight: 300; letter-spacing: 1px;
    line-height: 31.6px; height: 31.6px; white-space: nowrap;
  }
  .service-list li::before {
    content: ""; position: absolute; left: -20px; top: 9px; width: 10px; height: 10px; background: var(--ink);
  }
  .intro {
    position: absolute; left: 35px; top: 576px; width: 340px;
    font-family: "Hind", sans-serif; font-size: 15.5px; line-height: 22px; color: var(--ink); text-align: justify;
  }
  .badges { position: absolute; left: 18px; top: 672px; }
  .badge { position: absolute; background: #bdbdbd; }
  .postcard-front .photo { left: 403px; top: 0; width: 638px; height: 752px; }
  .web-strip { position: absolute; left: 1041px; top: 0; width: 79px; height: 503px; background: var(--paper); }
  .web-strip span {
    position: absolute; left: 50%; top: 250px;
    transform: translate(-50%, -50%) rotate(-90deg);
    font-size: 40px; font-weight: 300; color: var(--ink); white-space: nowrap;
  }
  .offer-band {
    position: absolute; left: 403px; top: 503px; width: 717px; height: 249px;
    background: var(--brand-green); opacity: 0.95; color: var(--paper);
  }
  .band-brand { position: absolute; left: 20px; top: 28px; display: flex; align-items: center; gap: 8px; }
  .band-brand .mark { width: 14px; height: 14px; background: var(--paper); }
  .band-brand span { font-size: 22px; font-weight: 400; letter-spacing: 1px; }
  .offer-title { position: absolute; left: 18px; top: 118px; font-family: "Hind", sans-serif; font-size: 48px; font-weight: 400; line-height: 1; }
  .offer-sub { position: absolute; left: 18px; top: 174px; font-family: "Hind", sans-serif; font-size: 19px; font-weight: 400; color: #e6e6e6; }
  .offer-value { position: absolute; left: 383px; top: 116px; font-family: "Hind", sans-serif; font-size: 80px; font-weight: 500; line-height: 1; white-space: nowrap; }
  .offer-value small { font-size: 48px; }
</style>
</head>
<body>
  <!-- Back side -->
  <article class="postcard postcard-back">
    <section class="contact-panel">
      <p class="brand-name">BrightCoat Crew</p>
      <div class="top-rule"></div>

      <svg class="contact-icon" style="top:108px" viewBox="0 0 22 22" aria-hidden="true">
        <circle cx="11" cy="11" r="11" fill="var(--icon)"/>
        <path d="M11 5a4 4 0 0 0-4 4c0 3 4 8 4 8s4-5 4-8a4 4 0 0 0-4-4z" fill="#fff"/>
        <circle cx="11" cy="9" r="1.5" fill="var(--icon)"/>
      </svg>
      <p class="contact-line address">4389 Juniper Ave #7, Waukesha,<br>WI 53947.</p>

      <svg class="contact-icon" style="top:208px" viewBox="0 0 22 22" aria-hidden="true">
        <circle cx="11" cy="11" r="11" fill="var(--icon)"/>
        <path d="M7.5 6l2 0 1 3-1.3 1a6 6 0 0 0 3 3l1-1.3 3 1 0 2a1.5 1.5 0 0 1-1.6 1.4A9 9 0 0 1 6 7.6 1.5 1.5 0 0 1 7.5 6z" fill="#fff"/>
      </svg>
      <p class="contact-line phone">262-555-0147</p>

      <svg class="contact-icon" style="top:296px" viewBox="0 0 22 22" aria-hidden="true">
        <circle cx="11" cy="11" r="11" fill="var(--icon)"/>
        <rect x="5.5" y="7" width="11" height="8" fill="#fff"/>
        <path d="M5.5 7l5.5 4.5L16.5 7" fill="none" stroke="var(--icon)" stroke-width="1.2"/>
      </svg>
      <p class="contact-line email">office@brightcoatcrew.example</p>

      <svg class="contact-icon" style="top:364px" viewBox="0 0 22 22" aria-hidden="true">
        <circle cx="11" cy="11" r="11" fill="var(--icon)"/>
        <circle cx="11" cy="11" r="5.5" fill="none" stroke="#fff" stroke-width="1.3"/>
        <path d="M5.5 11h11M11 5.5c-2.5 3-2.5 8 0 11M11 5.5c2.5 3 2.5 8 0 11" fill="none" stroke="#fff" stroke-width="1.1"/>
      </svg>
      <p class="contact-line web">www.BrightCoatCrew.example</p>
    </section>

    <section class="about-band">
      <p>Locally owned and operated, BrightCoat Crew serves most of Southeastern Wisconsin with friendly service through excellent work, fitting our crew to the size of your job, never more or less.</p>
    </section>

    <div class="photo" role="img" aria-label="Photo of two used paintbrushes with yellow and white paint on a wooden table"></div>

    <section class="cta-panel">
      <p>CONTACT US TODAY TO SCHEDULE YOUR FREE ESTIMATE</p>
    </section>
  </article>

  <!-- Front side -->
  <article class="postcard postcard-front">
    <section class="services-panel">
      <div class="top-rule"></div>
      <p class="eyebrow">WHAT</p>
      <h1 class="headline">WE DO</h1>
      <ul class="service-list">
        <li>INTERIOR PAINTING</li>
        <li>EXTERIOR PAINTING</li>
        <li>CARPENTRY SERVICES</li>
        <li>DRYWALL REPAIR</li>
        <li>COLOR CONSULTATIONS</li>
        <li>DECKS &amp; FENCES</li>
        <li>KITCHEN CABINETS</li>
        <li>SIDING AND TRIM REPAIR</li>
        <li>STAINING</li>
        <li>POWER WASHING</li>
        <li>PLASTER REPAIR</li>
        <li>INTERIOR TRIM</li>
      </ul>
      <p class="intro">We are a full service, one-stop-shop painting and carpentry company that can handle your complete project from start to finish.</p>
      <div class="badges" role="img" aria-label="Trade association and accreditation badges">
        <div class="badge" style="left:0;top:0;width:40px;height:68px;"></div>
        <div class="badge" style="left:80px;top:4px;width:56px;height:20px;"></div>
        <div class="badge" style="left:146px;top:4px;width:48px;height:20px;"></div>
        <div class="badge" style="left:82px;top:34px;width:52px;height:30px;"></div>
        <div class="badge" style="left:146px;top:34px;width:40px;height:30px;"></div>
        <div class="badge" style="left:196px;top:34px;width:34px;height:30px;"></div>
      </div>
    </section>

    <div class="photo" role="img" aria-label="Photo of used paintbrushes with colourful paint on a wooden table"></div>

    <div class="web-strip"><span>brightcoatcrew.example</span></div>

    <section class="offer-band">
      <div class="band-brand"><div class="mark"></div><span>BrightCoat Crew</span></div>
      <h2 class="offer-title">Spring Special</h2>
      <p class="offer-sub">Starting March, Interior &amp; Exterior</p>
      <p class="offer-value">15 <small>%</small> OFF</p>
    </section>
  </article>
</body>
</html>
```